Photography Business, Business Card

Looking for a unique cutting edge card that takes advantage of the latest printing technologies. Please review this site for all the options they office: https://plumeprints.example. If you can think it they can do it. And if you have an idea and do not know if they can do it, I will check into it.
Updates

Target Market(s)

People and places I took images of and future clients.

Industry/Entity Type

Photography

Contact Information for Business Card

Name, cell & email. Colin Hartley, chartley@kvnphoto.example, 318-742-9061

Colors

Designer to choose only greyscale colors for use in the design.

Requirements
Must have
• 100% cutting edge. Is so great, those I hand it to always show it to someone else. A piece of art.
Nice to have
• Blacks, silvers, greys, some red. Maybe other colors?

```html
<!DOCTYPE html>
<html lang="en">
<head>
<meta charset="utf-8">
<title>Colin Hartley — Photography Business Card</title>
<link rel="stylesheet" href="https://fonts.googleapis.com/css2?family=Montserrat:wght@600&display=swap">
<style>
  :root {
    --card-black: #050505;
    --script-grey: #1a1a1a;
    --lens-core: #020202;
    --lens-mid: #121212;
    --lens-edge: #242424;
    --ink-silver: #c8c8c8;
    --brand-red: #e51f29;
  }
  html, body {
    margin: 0;
    padding: 0;
    width: 1200px;
    height: 1200px;
    overflow: hidden;
    background: var(--card-black);
  }
  .card {
    position: relative;
    width: 1200px;
    height: 1200px;
    background: var(--card-black);
    overflow: hidden;
  }
  .script-backdrop {
    position: absolute;
    inset: 0;
    background: radial-gradient(ellipse at 50% 45%, var(--script-grey) 0%, var(--card-black) 78%);
  }
  .lens-photo {
    position: absolute;
    left: 279px;
    top: 253px;
    width: 642px;
    height: 642px;
    border-radius: 50%;
    background: radial-gradient(circle at 50% 50%, var(--lens-core) 0%, var(--lens-mid) 55%, var(--lens-edge) 88%, var(--card-black) 100%);
  }
  .ring-type {
    position: absolute;
    inset: 0;
  }
  .ring-text {
    font-family: "Montserrat", sans-serif;
    font-weight: 600;
    fill: var(--ink-silver);
  }
  .ring-text--name { font-size: 29px; letter-spacing: 16px; }
  .ring-text--phone { font-size: 26px; letter-spacing: 13px; }
  .ring-text--email { font-size: 21px; letter-spacing: 8px; }
  .brand-name {
    position: absolute;
    right: 62px;
    bottom: 89px;
    margin: 0;
    font-family: "Montserrat", sans-serif;
    font-weight: 600;
    font-size: 88px;
    letter-spacing: 28px;
    line-height: 0.72;
    color: var(--brand-red);
  }
</style>
</head>
<body>
  <main class="card">
    <div class="script-backdrop" role="img" aria-label="Faint repeated handwritten signature of the photographer's name across the background"></div>

    <div class="lens-photo" role="img" aria-label="Close-up photograph of a black camera lens seen head-on"></div>

    <svg class="ring-type" width="1200" height="1200" viewBox="0 0 1200 1200">
      <defs>
        <path id="arc-name" d="M350 512 A258 258 0 0 1 766 376"/>
        <path id="arc-phone" d="M607 389 A185 185 0 0 1 742 693"/>
        <path id="arc-email" d="M340 654 A272 272 0 0 0 836 710"/>
      </defs>
      <text class="ring-text ring-text--name"><textPath href="#arc-name">COLIN HARTLEY</textPath></text>
      <text class="ring-text ring-text--phone"><textPath href="#arc-phone">318-742-9061</textPath></text>
      <text class="ring-text ring-text--email"><textPath href="#arc-email">CHARTLEY@KVNPHOTO.EXAMPLE</textPath></text>
    </svg>

    <p class="brand-name">KVN</p>
  </main>
</body>
</html>
```